Business Card/ Email Signature Design Project

I am an Interior Designer. I need a business card that looks sophisticated stylish but simple in design. My work covers space design/ interior architecture/ furniture design/ product development & styling.

I have a very specific brief and know mostly what I want. I'm hoping to work with someone who can translate my ideas.

My branding should have a strong focus on my name, the majority of my work is referral based.
I'm keen to keep a monochromatic colour scheme: dark charcoal/ black/ white/ embossing/ silver. I'm not suggesting we use all that I've listed, they are possible ideas at this stage. I will need to be mindful of printing costs an also how I make the design work across, cards, letter heads, email logo and web design.

Theory behind images sent below;
1-Rug Image_(minus boarder) I was thinking this image could be used on the back of the card with my contact details over. I like that the lines are almost hand drawn and start to look free form. It's a subtle contrast to a more formal front of the card with my name.
2_Tomas Ferle_I really like the orientation, the proportion of font on the card, the colour and the font. I like the lower case for my name and the upper case for 'Interior Design'. Not sure if it should be 'Interior Designer or Interior Design' at this stage, was leaning towards 'Interior Design'. Was thinking the 'i' and 'd' in my surname could be the colour eg 'silver'?? We can decide on this once we see it.

Look forward to hearing from you.
Cheers,
Saskia Bremond

Printing

Saskia Bremond Interior Design

```html
<!DOCTYPE html>
<html lang="en">
<head>
<meta charset="utf-8">
<title>Saskia Bremond Interior Design – Business Card</title>
<link href="https://fonts.googleapis.com/css2?family=Montserrat:wght@200;400;600;700&display=swap" rel="stylesheet">
<style>
  :root {
    --backdrop: #eceeee;
    --card: #1b1b1b;
    --card-edge: #262626;
    --white: #ffffff;
    --silver: #c9c9c9;
    --line-art: #2c2c2c;
  }
  * { margin: 0; padding: 0; box-sizing: border-box; }
  html, body {
    width: 1200px; height: 408px; overflow: hidden;
    background: var(--backdrop);
    font-family: "Montserrat", sans-serif;
  }
  .canvas { position: relative; width: 1200px; height: 408px; }

  .card {
    position: absolute; top: 52px;
    width: 533px; height: 300px;
    border-radius: 20px;
    background: var(--card);
    border: 1px solid var(--card-edge);
    overflow: hidden;
    color: var(--white);
  }
  .card--front { left: 42px; }
  .card--back  { left: 610px; }

  /* Front */
  .brand-name {
    position: absolute; left: 50px; top: 78px;
    font-size: 52px; font-weight: 600; letter-spacing: 0.5px;
    line-height: 1; color: var(--white);
  }
  .brand-rule {
    position: absolute; left: 50px; top: 150px;
    width: 430px; height: 2px; background: var(--white);
  }
  .brand-tagline {
    position: absolute; left: 48px; top: 164px;
    font-size: 41px; font-weight: 200; letter-spacing: 0.5px;
    line-height: 1; color: var(--silver);
  }

  /* Back */
  .contact-name {
    position: absolute; left: 42px; top: 42px;
    font-size: 19px; font-weight: 600; line-height: 1;
  }
  .contact-list { position: absolute; left: 44px; top: 72px; list-style: none; }
  .contact-item {
    display: flex; align-items: center; gap: 12px;
    height: 27px; font-size: 14px; font-weight: 600;
  }
  .contact-item--address { font-weight: 400; font-size: 13.5px; }
  .contact-icon { width: 16px; height: 16px; flex: none; }
  .room-sketch {
    position: absolute; left: 158px; top: 80px;
    width: 370px; height: 200px;
    background: linear-gradient(160deg, var(--line-art) 0%, var(--card) 85%);
    border-radius: 4px;
  }
</style>
</head>
<body>
<div class="canvas">

  <section class="card card--front">
    <h1 class="brand-name">saskia bremond</h1>
    <div class="brand-rule"></div>
    <p class="brand-tagline">INTERIOR DESIGN</p>
  </section>

  <section class="card card--back">
    <div class="room-sketch" role="img" aria-label="White line drawing of a living room with sofa, dining chairs and windows"></div>
    <h2 class="contact-name">Saskia Bremond</h2>
    <ul class="contact-list">
      <li class="contact-item">
        <svg class="contact-icon" viewBox="0 0 16 16" fill="none" stroke="#fff" stroke-width="1.2"><rect x="4" y="1" width="8" height="14" rx="1.5"/><line x1="7" y1="13" x2="9" y2="13"/></svg>
        0400 555 018
      </li>
      <li class="contact-item">
        <svg class="contact-icon" viewBox="0 0 16 16" fill="none" stroke="#fff" stroke-width="1.2"><rect x="1" y="3.5" width="14" height="9"/><polyline points="1,3.5 8,9 15,3.5"/></svg>
        interiors@saskiabremond.com
      </li>
      <li class="contact-item">
        <svg class="contact-icon" viewBox="0 0 16 16" fill="none" stroke="#fff" stroke-width="1.2"><circle cx="8" cy="8" r="6.5"/><ellipse cx="8" cy="8" rx="3" ry="6.5"/><line x1="1.5" y1="8" x2="14.5" y2="8"/></svg>
        www.saskiabremond.com
      </li>
      <li class="contact-item contact-item--address">
        <svg class="contact-icon" viewBox="0 0 16 16" fill="none" stroke="#fff" stroke-width="1.2"><path d="M8 15 C8 15 3 9.5 3 6 A5 5 0 0 1 13 6 C13 9.5 8 15 8 15Z"/><circle cx="8" cy="6" r="1.8"/></svg>
        P.O Box 214 Elmhurst VIC. 3999
      </li>
    </ul>
  </section>

</div>
</body>
</html>
```